TBNW site redesign

Please redesign a home page with content provided. PSD only - no coding
Can use any images from Vexelmarq.com

Please create a site design that more clearly illustrates the client's services and expertise. We are looking for a high-end design.

Any images used must be generic or of Dallas TX.

Fonts: Any
Colors: Match to logo
Look: Modern - Professional

Target Market(s)

medium-large business owners

Number of Pages Required

1 page

Font styles to use
Serif
Sans Serif

Requirements
Must have
• cohesive professional design
• high end look
• Match to logo

```html
<!DOCTYPE html>
<html lang="en">
<head>
<meta charset="utf-8">
<title>TBNW – Home</title>
<link rel="stylesheet" href="https://fonts.googleapis.com/css2?family=Cinzel:wght@700&family=Arimo:wght@400&display=swap">
<style>
  :root {
    --brand-red: #d12128;
    --ink: #161616;
    --page: #ffffff;
    --backdrop: #f1f1f2;
    --on-red: #ffffff;
  }
  * { margin: 0; padding: 0; box-sizing: border-box; }
  html, body { width: 1200px; height: 1000px; overflow: hidden; }
  body { background: var(--backdrop); font-family: "Arimo", Arial, sans-serif; color: var(--ink); position: relative; }

  .home-page { position: absolute; left: 0; top: 125px; width: 1200px; height: 749px; background: var(--page); }
  .section-title {
    position: absolute; left: 66px;
    font-family: "Cinzel", "Times New Roman", serif; font-weight: 700;
    font-size: 30px; color: var(--brand-red); line-height: 1; letter-spacing: 2.4px;
  }
  .section-title--testimonial { top: 2px; }
  .section-title--articles { top: 358px; }

  .text { position: absolute; font-size: 22px; line-height: 23px; white-space: nowrap; }
  .testimonial-quote { left: 72px; top: 62px; font-size: 21px; line-height: 21px; }
  .testimonial-author { left: 67px; top: 161px; }
  .cta-line-1 { left: 72px; top: 211px; }
  .cta-line-2 { left: 75px; top: 252px; }
  .cta-appointment { left: 75px; top: 287px; }
  .contact-heading { left: 72px; top: 421px; }
  .contact-address { left: 72px; top: 456px; }
  .contact-phone { left: 74px; top: 509px; }

  .site-footer { position: absolute; left: 0; bottom: 0; width: 1200px; height: 150px; background: var(--brand-red); }
  .footer-brand {
    position: absolute; top: 32px; width: 165px; height: 66px;
    display: flex; align-items: center; justify-content: center; gap: 10px;
    color: var(--on-red); font-size: 30px; letter-spacing: 2px;
  }
  .footer-brand .brand-square { width: 14px; height: 14px; background: var(--on-red); }
  .footer-brand--left { left: 73px; }
  .footer-brand--right { left: 993px; }
  .footer-notices { position: absolute; left: 0; width: 1200px; top: 37px; text-align: center; list-style: none; }
  .footer-notices li { color: var(--on-red); font-size: 15px; line-height: 15px; margin-bottom: 15px; }
</style>
</head>
<body>
  <main class="home-page">
    <h2 class="section-title section-title--testimonial">Client testimonial</h2>
    <p class="text testimonial-quote">“The real estate team at TBNW has decades of experience in Commercial. One advantage of TBNW is<br>they know all the properties that are about to become available, BEFORE they are available. They have<br>the inside track on properties and they watch your back at the negotiating table. Very&nbsp; impressive with a<br>polished approach. Let the team run with your next project and you won't be disappointed.”</p>
    <p class="text testimonial-author">-Marcus Allen Whitfield</p>

    <p class="text cta-line-1">Whether your lease is expiring soon, or you're just starting your search,</p>
    <p class="text cta-line-2">TBNW can help you find the perfect space.</p>
    <p class="text cta-appointment">- MAKE AN APPOINTMENT -</p>

    <h2 class="section-title section-title--articles">Recent articles</h2>
    <p class="text contact-heading">Contact Information :</p>
    <p class="text contact-address">412 Cedar Ridge Avenue, Suite 610,<br>Dallas, TX 75201</p>
    <p class="text contact-phone">Tel : 214-555-0142<br>Fax : 214-555-0187</p>

    <footer class="site-footer">
      <div class="footer-brand footer-brand--left"><span class="brand-square"></span>TBNW</div>
      <ul class="footer-notices">
        <li>State Realty Board Mandated Disclosure Notices</li>
        <li>State Realty Board Consumer Protection Notice</li>
        <li>State Realty Board Information About Brokerage Services</li>
      </ul>
      <div class="footer-brand footer-brand--right"><span class="brand-square"></span>TBNW</div>
    </footer>
  </main>
</body>
</html>
```